RB Cargonet businesscard project

RB Cargonet Ltd is a freshly founded small (3 employees), young (average age is 30 years) company, living from the road transportation market without own tools.
We would like to have an impressive, new-line, cool busines card for a freshly founded forwarding company on an overcrowded market which raises attention and makes the potential partners eager to work with us.

Our logo is in the attachment, please use it for the card.

Target Market(s)

The main profile of the company is logistic/forwarding on road.

Industry/Entity Type

Freight Forwarding

Contact Information for Business Card

Name: Varga Edina
Title: general manager
mobile nr: +36-70/482-5910
fax nr: +36-1/655-3947
e-mail: edina.varga@rbcargonet-example.com
info@rbcargonet-example.com
website address: http://www.rbcargonet-example.com
and if possible maybe some funny or helpful info on the back

Requirements
Must have
• contact details above
Nice to have
• some really nice and catching back-side (info, graphics, useful tool info... anything)
Should not have
• trucks, road, ship, airplane on it...

```html
<!DOCTYPE html>
<html lang="en">
<head>
<meta charset="utf-8">
<title>RB Cargonet – Business Card</title>
<link href="https://fonts.googleapis.com/css2?family=Open+Sans:wght@400;600&display=swap" rel="stylesheet">
<style>
  :root {
    --page: #e9e6e1;
    --card-white: #f4f6f8;
    --card-blue: #5580b8;
    --ink: #1e2530;
    --ink-soft: #2b3442;
    --logo-ink: #3a3a3a;
    --accent: #5580b8;
  }
  * { margin: 0; padding: 0; box-sizing: border-box; }
  html, body {
    width: 1200px; height: 902px; overflow: hidden;
    background: var(--page);
    font-family: "Open Sans", Arial, sans-serif;
  }
  .canvas {
    position: relative; width: 1200px; height: 902px;
    display: flex; align-items: center; justify-content: center;
  }
  .business-card {
    position: relative; width: 1000px; height: 572px;
    background: var(--card-white);
    box-shadow: 0 14px 40px rgba(0,0,0,.22);
    overflow: hidden;
  }
  .card-band { position: absolute; inset: 0; width: 100%; height: 100%; }
  .brand {
    position: absolute; left: 395px; top: 150px;
    display: flex; align-items: center; gap: 16px;
  }
  .brand-mark { width: 34px; height: 34px; background: var(--accent); }
  .brand-name {
    font-size: 52px; font-weight: 600; color: var(--logo-ink);
    letter-spacing: -0.5px; line-height: 1;
  }
  .holder { position: absolute; left: 70px; top: 410px; }
  .holder-name { font-size: 56px; font-weight: 400; color: var(--ink); line-height: 1.05; }
  .holder-title { font-size: 22px; color: var(--ink-soft); margin-left: 92px; margin-top: 2px; }
  .divider {
    position: absolute; left: 585px; top: 290px;
    width: 2px; height: 180px; background: var(--ink);
  }
  .contact-list {
    position: absolute; left: 610px; top: 290px; list-style: none;
  }
  .contact-item {
    display: flex; align-items: center; gap: 12px;
    font-size: 20px; color: var(--ink); line-height: 35px;
  }
  .contact-icon { width: 18px; height: 18px; flex: none; }
</style>
</head>
<body>
<main class="canvas">
  <section class="business-card" aria-label="RB Cargonet business card">
    <svg class="card-band" viewBox="0 0 1000 572" preserveAspectRatio="none" aria-hidden="true">
      <path d="M0 455 C 320 400, 720 330, 1000 120 L1000 572 L0 572 Z" fill="var(--card-blue)"/>
    </svg>

    <div class="brand">
      <span class="brand-mark"></span>
      <span class="brand-name">RB Cargonet</span>
    </div>

    <div class="divider"></div>

    <ul class="contact-list">
      <li class="contact-item">
        <svg class="contact-icon" viewBox="0 0 18 18"><rect width="18" height="18" fill="var(--ink)"/><path d="M5 4l2 0 1 3-1.5 1a6 6 0 0 0 3.5 3.5L11 10l3 1v2a1 1 0 0 1-1 1A9 9 0 0 1 4 5a1 1 0 0 1 1-1z" fill="#fff"/></svg>
        +36-70/482-5910
      </li>
      <li class="contact-item">
        <svg class="contact-icon" viewBox="0 0 18 18"><rect width="18" height="18" fill="var(--ink)"/><rect x="4" y="7" width="10" height="7" fill="#fff"/><rect x="6" y="3" width="6" height="4" fill="#fff"/></svg>
        +36-1/655-3947
      </li>
      <li class="contact-item">
        <svg class="contact-icon" viewBox="0 0 18 18"><rect width="18" height="18" fill="var(--ink)"/><rect x="3.5" y="5" width="11" height="8" fill="#fff"/><path d="M3.5 5l5.5 4.5L14.5 5" fill="none" stroke="var(--ink)" stroke-width="1.2"/></svg>
        info@rbcargonet-example.com
      </li>
      <li class="contact-item">
        <svg class="contact-icon" viewBox="0 0 18 18"><rect width="18" height="18" fill="var(--ink)"/><circle cx="9" cy="9" r="5" fill="none" stroke="#fff" stroke-width="1.4"/><path d="M4 9h10M9 4c-2.5 3-2.5 7 0 10M9 4c2.5 3 2.5 7 0 10" fill="none" stroke="#fff" stroke-width="1"/></svg>
        http://www.rbcargonet-example.com
      </li>
      <li class="contact-item">
        <svg class="contact-icon" viewBox="0 0 18 18"><rect width="18" height="18" fill="var(--ink)"/><rect x="3.5" y="5" width="11" height="8" fill="#fff"/><path d="M3.5 5l5.5 4.5L14.5 5" fill="none" stroke="var(--ink)" stroke-width="1.2"/></svg>
        edina.varga@rbcargonet-example.com
      </li>
    </ul>

    <div class="holder">
      <p class="holder-name">Varga Edina</p>
      <p class="holder-title">general manager</p>
    </div>
  </section>
</main>
</body>
</html>
```